Sunscreen Package Design Modern SPF 50

Update current package design to a more modern design target women 16-40 Do not make it playful. SOLANA CREST is home to movie stars and high income business people PalmSprings is one of the most desired vacation areas in the world. The sun shines 350 days a year. World class Tennis and Golf tournaments are held every year with the worlds top players attending these tournaments

Target Market(s)

Women

Industry/Entity Type

Skin Protection

Font styles to use
Sans Serif

Requirements
Must have
• The words SOLANA CREST and VELORIMA

```html
<!DOCTYPE html>
<html lang="en">
<head>
<meta charset="utf-8">
<title>Solana Crest Velorima Aftersun – Label Designs</title>
<link rel="stylesheet" href="https://fonts.googleapis.com/css2?family=Montserrat:wght@400&display=swap">
<style>
  :root{
    --bg:#ececec;
    --cream:#f4f0e8;
    --cream-light:#f7f4ee;
    --teal:#a4d3d2;
    --teal-soft:#cfe4dd;
    --gold:#c6a25f;
    --gold-deep:#b48e4c;
    --gold-light:#d8b978;
    --ink:#35383a;
    --ink-soft:#55585a;
  }
  *{box-sizing:border-box;margin:0;padding:0}
  html,body{width:1200px;height:1200px;overflow:hidden;background:var(--bg)}
  .stage{position:relative;width:1200px;height:1200px;display:flex;justify-content:center;align-items:center;gap:80px}
  .label{
    position:relative;width:380px;height:1000px;
    display:flex;flex-direction:column;align-items:center;
    padding-top:90px;text-align:center;
    border-radius:6px;overflow:hidden;
    font-family:"Montserrat",sans-serif;font-weight:400;
  }
  .label--cream{background:var(--cream)}
  .label--teal{background:linear-gradient(180deg,var(--cream-light) 0%,var(--cream-light) 38%,var(--teal-soft) 62%,var(--teal) 100%)}
  .brand-spot{width:86px;height:86px;border-radius:50%;background:var(--gold);margin-bottom:46px}
  .brand-name{
    font-size:44px;font-weight:400;line-height:1.12;letter-spacing:2px;color:var(--ink);
  }
  .brand-name span{display:block;font-size:17px;letter-spacing:6px;margin-top:14px}
  .divider{width:46px;height:2px;background:var(--gold);margin:34px 0 36px}
  .product-name{
    font-size:24px;font-weight:400;letter-spacing:8px;color:var(--ink);margin-bottom:14px;
  }
  .claim,.ingredients{
    color:var(--ink-soft);font-size:12px;letter-spacing:2.4px;line-height:1.5;text-transform:uppercase;
  }
  .ingredients{margin-top:16px;line-height:1.65}
  .scene{
    position:absolute;left:0;right:0;bottom:150px;height:200px;
    background:linear-gradient(180deg,rgba(198,162,95,0) 0%,rgba(198,162,95,.35) 55%,rgba(198,162,95,.5) 100%);
  }
  .label--teal .scene{bottom:170px;height:190px;background:linear-gradient(180deg,rgba(198,162,95,0) 0%,rgba(198,162,95,.4) 100%)}
  .footer{
    position:absolute;left:0;right:0;bottom:0;height:150px;
    display:flex;flex-direction:column;align-items:center;padding-top:26px;color:var(--ink-soft);
  }
  .tagline{font-size:12px;letter-spacing:3px;padding-bottom:14px;border-bottom:2px solid var(--gold);width:300px}
  .volume{font-size:11px;letter-spacing:3px;margin-top:22px}
  .label--teal .footer{height:170px;padding-top:0}
  .gold-band{
    width:100%;height:56px;display:flex;align-items:center;justify-content:center;
    background:linear-gradient(90deg,var(--gold-deep),var(--gold-light) 50%,var(--gold-deep));
    font-size:12px;letter-spacing:3px;color:var(--ink);
  }
</style>
</head>
<body>
<main class="stage">
  <section class="label label--cream">
    <div class="brand-spot"></div>
    <h1 class="brand-name">SOLANA<br>CREST<span>VELORIMA</span></h1>
    <div class="divider"></div>
    <h2 class="product-name">AFTERSUN</h2>
    <p class="claim">Hydrate skin with these<br>essential ingredients</p>
    <p class="ingredients">Hyaluronate acid<br>Cucumber<br>Aloe + Jojoba<br>Sunflower</p>
    <div class="scene" role="img" aria-label="Gold line illustration of palm trees and desert mountains"></div>
    <div class="footer">
      <p class="tagline">SUNLIT DUNE SKINCARE</p>
      <p class="volume">3 FL OZ / 88 mL</p>
    </div>
  </section>

  <section class="label label--teal">
    <div class="brand-spot"></div>
    <h1 class="brand-name">SOLANA<br>CREST<span>VELORIMA</span></h1>
    <div class="divider"></div>
    <h2 class="product-name">AFTERSUN</h2>
    <p class="claim">Hydrate skin with these<br>essential ingredients</p>
    <p class="ingredients">Hyaluronate acid<br>Cucumber<br>Aloe + Jojoba<br>Sunflower</p>
    <div class="scene" role="img" aria-label="Gold line illustration of palm trees and desert mountains"></div>
    <div class="footer">
      <p class="gold-band">SUNLIT DUNE SKINCARE</p>
      <p class="volume">3 FL OZ / 88 mL</p>
    </div>
  </section>
</main>
</body>
</html>
```